Brightmark Electrical Flyer

An eye catching flyer design which showcases the type of work we do in the electrical industry in Vancouver,BC. The final design should be simple and incorporate our logo. And present a high end company.

Industry/Entity Type

Electrical

```html
<!DOCTYPE html>
<html lang="en">
<head>
<meta charset="utf-8">
<title>Brightmark Electrical Flyer</title>
<link href="https://fonts.googleapis.com/css2?family=Oswald:wght@600;700&family=Titillium+Web:wght@400;600&family=Open+Sans:wght@400;600;700&display=swap" rel="stylesheet">
<style>
:root{
  --backdrop:#8a5f3d;
  --yellow:#f5d000;
  --gold:#d9a20c;
  --ink:#2b2b2b;
  --band:#3a3a3a;
  --white:#ffffff;
}
*{margin:0;padding:0;box-sizing:border-box}
html,body{width:971px;height:1200px;overflow:hidden;background:var(--backdrop)}
.flyer{position:absolute;left:36px;top:18px;width:954px;height:1232px;transform:scale(0.944);transform-origin:0 0;background:var(--white);overflow:hidden;box-shadow:0 6px 14px rgba(0,0,0,.35)}
.hero-photo{position:absolute;left:0;top:0;width:954px;height:771px;background:linear-gradient(180deg,#ffffff 0%,#f7f9fb 35%,#dfe7ee 58%,#c9d3dc 78%,#eceff2 100%)}
.brand{position:absolute;left:45px;top:88px;display:flex;align-items:center;gap:12px;font-family:"Titillium Web",sans-serif;font-weight:600;font-size:34px;color:var(--ink)}
.brand-mark{width:26px;height:26px;background:var(--yellow)}
.headline{position:absolute;right:54px;top:62px;text-align:right;font-family:"Oswald",sans-serif;font-weight:700;font-size:54px;line-height:59px;color:var(--yellow);-webkit-text-stroke:1.2px #6b5300;text-transform:uppercase}
.services-banner{position:absolute;left:0;top:229px;width:390px;height:58px;border-radius:0 29px 29px 0;background:linear-gradient(90deg,var(--yellow),var(--gold));font-family:"Titillium Web",sans-serif;font-weight:600;font-size:31px;line-height:58px;padding-left:52px;color:var(--ink)}
.service-list{position:absolute;left:52px;top:308px;display:grid;grid-template-columns:203px 240px;row-gap:8px;list-style:none;font-family:"Titillium Web",sans-serif;font-weight:600;font-size:23px;color:var(--ink)}
.service-list li{display:flex;align-items:center;gap:10px;height:30px}
.service-list svg{width:22px;height:22px;flex:none}
.web-tab{position:absolute;left:18px;top:720px;width:504px;height:68px}
.web-tab svg{position:absolute;inset:0}
.web-tab span{position:absolute;left:54px;top:10px;font-family:"Oswald",sans-serif;font-weight:600;font-size:35px;color:var(--white);letter-spacing:.5px}
.info-band{position:absolute;left:0;top:771px;width:954px;height:461px;background:var(--band)}
.intro{position:absolute;right:61px;top:800px;width:640px;text-align:right;font-family:"Open Sans",sans-serif;font-weight:600;font-size:16px;line-height:23px;color:var(--white)}
.about{position:absolute;left:50px;top:860px;width:110px;font-family:"Open Sans",sans-serif;font-weight:600;font-size:16.5px;line-height:23.4px;color:var(--white)}
.card{position:absolute;top:864px;width:238px;height:289px;background:var(--yellow);padding:8px;text-align:center;font-family:"Open Sans",sans-serif;color:var(--ink)}
.card-photo{width:222px;height:148px;border-radius:8px;border:2px solid var(--white)}
.card h3{margin-top:10px;font-weight:600;font-size:16px;line-height:20px}
.card p{margin-top:6px;font-size:11.5px;line-height:17px}
.card-justify p{text-align:justify;text-align-last:center}
.contact-email{position:absolute;left:162px;top:1172px;font-family:"Open Sans",sans-serif;font-weight:600;font-size:20px;color:var(--white)}
.contact-phone{position:absolute;right:49px;top:1168px;font-family:"Open Sans",sans-serif;font-weight:700;font-size:25px;color:var(--white)}
</style>
</head>
<body>
<main class="flyer">
  <div class="hero-photo" role="img" aria-label="Bright modern living room with white sofa, fireplace, yellow poufs and pool view"></div>

  <div class="brand"><span class="brand-mark"></span>Brightmark Electrical Inc</div>

  <h1 class="headline">Residential<br>Commercial<br>and Industrial<br>Electrical<br>Services</h1>

  <div class="services-banner">TYPES OF SERVICES</div>
  <ul class="service-list">
    <li><svg viewBox="0 0 22 22"><rect x="1" y="3" width="18" height="18" fill="#fff" stroke="#6b5300" stroke-width="2"/><path d="M5 11l4 5 11-14" fill="none" stroke="#e0a800" stroke-width="3"/></svg>Residential</li>
    <li><svg viewBox="0 0 22 22"><rect x="1" y="3" width="18" height="18" fill="#fff" stroke="#6b5300" stroke-width="2"/><path d="M5 11l4 5 11-14" fill="none" stroke="#e0a800" stroke-width="3"/></svg>Commerical</li>
    <li><svg viewBox="0 0 22 22"><rect x="1" y="3" width="18" height="18" fill="#fff" stroke="#6b5300" stroke-width="2"/><path d="M5 11l4 5 11-14" fill="none" stroke="#e0a800" stroke-width="3"/></svg>industrial</li>
    <li><svg viewBox="0 0 22 22"><rect x="1" y="3" width="18" height="18" fill="#fff" stroke="#6b5300" stroke-width="2"/><path d="M5 11l4 5 11-14" fill="none" stroke="#e0a800" stroke-width="3"/></svg>Lighting</li>
    <li><svg viewBox="0 0 22 22"><rect x="1" y="3" width="18" height="18" fill="#fff" stroke="#6b5300" stroke-width="2"/><path d="M5 11l4 5 11-14" fill="none" stroke="#e0a800" stroke-width="3"/></svg>Fire Alarm</li>
    <li><svg viewBox="0 0 22 22"><rect x="1" y="3" width="18" height="18" fill="#fff" stroke="#6b5300" stroke-width="2"/><path d="M5 11l4 5 11-14" fill="none" stroke="#e0a800" stroke-width="3"/></svg>Low Voltage Wiring</li>
    <li><svg viewBox="0 0 22 22"><rect x="1" y="3" width="18" height="18" fill="#fff" stroke="#6b5300" stroke-width="2"/><path d="M5 11l4 5 11-14" fill="none" stroke="#e0a800" stroke-width="3"/></svg>Security</li>
    <li><svg viewBox="0 0 22 22"><rect x="1" y="3" width="18" height="18" fill="#fff" stroke="#6b5300" stroke-width="2"/><path d="M5 11l4 5 11-14" fill="none" stroke="#e0a800" stroke-width="3"/></svg>Solar Panel</li>
  </ul>

  <section class="info-band"></section>

  <div class="web-tab">
    <svg viewBox="0 0 504 68" width="504" height="68">
      <defs><linearGradient id="tabFill" x1="0" x2="1"><stop offset="0" stop-color="#f5d000"/><stop offset="1" stop-color="#d9a20c"/></linearGradient></defs>
      <path d="M0 68 L40 0 H430 L504 60 V68 Z" fill="url(#tabFill)"/>
    </svg>
    <span>BRIGHTMARKELECTRICAL.CA</span>
  </div>

  <p class="intro">Brightmark Electrical offers a wide varierty of services, to meet your electrical needs. Whether it may be residential, commercial or industrial.</p>

  <p class="about">We are an electrical contractor serving the lower mainland. Providing the best in customer service and knowledge, to our clients.</p>

  <article class="card" style="left:163px">
    <div class="card-photo" role="img" aria-label="Colourful lit hallway with red and yellow lighting" style="background:linear-gradient(135deg,#6a2a1a,#e0a020 45%,#c8281e)"></div>
    <h3>LIGHTING<br>EXPERTS</h3>
    <p>We provide all your lighting needs to complete any project from small to large</p>
  </article>
  <article class="card" style="left:414px">
    <div class="card-photo" role="img" aria-label="Open smart lighting electrical panel" style="background:linear-gradient(90deg,#d8d8d8 0 20%,#1e1e22 20% 62%,#cfd3d6 62%)"></div>
    <h3>PANELIZED SMART<br>LIGHTING</h3>
    <p>Smart lighting solutions give you endless options with your lights</p>
  </article>
  <article class="card card-justify" style="left:666px">
    <div class="card-photo" role="img" aria-label="Electrician holding a yellow hard hat and phone" style="background:linear-gradient(135deg,#9a4a3a,#d8c9b0 50%,#e8c400)"></div>
    <h3>QUALITY ON TIME<br>CONSTRUCTION</h3>
    <p>We efficiently manage construction and co odinate with schedules to always give our clients an effortless experience.</p>
  </article>

  <div class="contact-email">info@BRIGHTMARKELECTRICAL.CA</div>
  <div class="contact-phone">Contact us: 604 555 0187</div>
</main>
</body>
</html>
```